Website for new dental office

I am Dr. Colin Marsh and am building a new dental practice. I specialize in general dentistry. I am young and have a higher end dental practice incorporating very new technologies and would like my website to reflect that. As many dental patients are older, the website must be very easy to navigate. I would like patients to be able to request appointments, and will eventually add on patient information forms (the health history, etc, that you normally fill out in the practice) from my practice management software, so leave an area for that.

Industry/Entity Type

Building

```html
<!DOCTYPE html>
<html lang="en">
<head>
<meta charset="utf-8">
<title>Marsh Dental</title>
<link rel="stylesheet" href="https://fonts.googleapis.com/css2?family=Tinos:wght@400;700&display=swap">
<style>
  :root {
    --page-bg: #ffffff;
    --ink: #111111;
    --nav-active: #8a8a8a;
    --photo-light: #d9d9d9;
    --photo-mid: #a8a8a8;
    --photo-dark: #5e5e5e;
    --hero-text: #ffffff;
    --button-bg: rgba(235, 235, 235, 0.55);
  }
  * { margin: 0; padding: 0; box-sizing: border-box; }
  html, body {
    width: 1200px;
    height: 900px;
    overflow: hidden;
    background: var(--page-bg);
    font-family: "Tinos", "Times New Roman", serif;
    color: var(--ink);
  }
  .site {
    position: relative;
    width: 1200px;
    height: 900px;
    display: flex;
  }
  .sidebar {
    position: relative;
    width: 389px;
    height: 900px;
    background: var(--page-bg);
  }
  .brand {
    position: absolute;
    left: 42px;
    top: 46px;
    font-size: 34px;
    font-weight: 400;
    color: var(--ink);
    letter-spacing: 0.2px;
  }
  .main-nav {
    position: absolute;
    left: 42px;
    top: 299px;
    list-style: none;
  }
  .main-nav li {
    height: 44.5px;
    font-size: 18.5px;
    text-transform: uppercase;
    letter-spacing: 0.2px;
  }
  .main-nav a { color: var(--ink); text-decoration: none; }
  .main-nav .is-active a { color: var(--nav-active); }

  .hero {
    position: relative;
    flex: 1;
    height: 900px;
    overflow: hidden;
  }
  .hero-photo {
    position: absolute;
    inset: 0;
    background:
      radial-gradient(ellipse 55% 30% at 58% 60%, var(--photo-dark) 0%, rgba(94,94,94,0) 70%),
      radial-gradient(ellipse 60% 45% at 30% 20%, var(--photo-light) 0%, rgba(217,217,217,0) 75%),
      linear-gradient(160deg, var(--photo-light) 0%, var(--photo-mid) 55%, #bdbdbd 100%);
  }
  .contact-card {
    position: absolute;
    right: 68px;
    top: 292px;
    text-align: right;
    color: var(--hero-text);
    font-size: 26px;
    line-height: 34px;
  }
  .contact-card .doctor { margin-bottom: 34px; }
  .contact-card .doctor strong { font-weight: 700; }
  .appointment-button {
    position: absolute;
    right: 68px;
    top: 574px;
    width: 248px;
    height: 68px;
    background: var(--button-bg);
    color: var(--ink);
    font-size: 17.5px;
    display: flex;
    align-items: center;
    justify-content: center;
    text-decoration: none;
  }
  .copyright {
    position: absolute;
    right: 68px;
    top: 856px;
    color: var(--hero-text);
    font-size: 12.5px;
    word-spacing: 2px;
  }
</style>
</head>
<body>
<div class="site">
  <aside class="sidebar">
    <div class="brand">Marsh Dental</div>
    <ul class="main-nav">
      <li><a href="#">Team</a></li>
      <li><a href="#">Services</a></li>
      <li class="is-active"><a href="#">Portfolio</a></li>
      <li><a href="#">Our Office</a></li>
      <li><a href="#">Patient</a></li>
      <li><a href="#">Resources</a></li>
      <li><a href="#">Contact Us</a></li>
    </ul>
  </aside>
  <main class="hero">
    <div class="hero-photo" role="img" aria-label="Black and white close-up photograph of a smiling mouth with bright teeth"></div>
    <div class="contact-card">
      <p class="doctor"><strong>Colin Marsh</strong>&nbsp; (DDS)</p>
      <p>Phone : 617-555-0142</p>
      <p>Email : colin.marsh@example.com</p>
    </div>
    <a class="appointment-button" href="#">Request An Appointment</a>
    <p class="copyright">Copyright : Colin Marsh &nbsp; 2014</p>
  </main>
</div>
</body>
</html>
```